Q-Rolls Business Card

We are a modern retail clothing store. Established in 1994. I need a presentable card that will amaze vendors when given to them.

Front: Logo in middle
Info Side:

Name: Tomas Velder
Cell: 630-812-4463
Work: 630-917-3384 EXT. 417
Email: Tomas@q-rolls-example.com
Website: www.Q-rolls-example.com

Industry/Entity Type

Business

```html
<!DOCTYPE html>
<html lang="en">
<head>
<meta charset="utf-8">
<title>Q-Rolls Business Card</title>
<link rel="stylesheet" href="https://fonts.googleapis.com/css2?family=Arimo:wght@400;700&display=swap">
<style>
  :root {
    --backdrop: #e9e6e1;
    --front-card: #b3b3b3;
    --back-card: #0b0b0b;
    --ink-light: #ffffff;
    --ink-soft: #d9d9d9;
    --rule: #f2f2f2;
  }
  * { margin: 0; padding: 0; box-sizing: border-box; }
  html, body {
    width: 1200px;
    height: 950px;
    overflow: hidden;
    background: var(--backdrop);
    font-family: "Arimo", Arial, sans-serif;
  }
  .canvas { position: relative; width: 1200px; height: 950px; }

  .card {
    position: absolute;
    width: 620px;
    height: 354px;
    border-radius: 4px;
    box-shadow: 0 10px 28px rgba(0,0,0,0.25);
  }

  /* Front side */
  .card--front {
    left: 110px;
    top: 80px;
    background: var(--front-card);
  }
  .card--front .brand-name {
    position: absolute;
    left: 0; right: 0;
    top: 120px;
    text-align: center;
    font-weight: 700;
    font-size: 58px;
    letter-spacing: 2px;
    color: var(--ink-light);
  }
  .card--front .web-line {
    position: absolute;
    left: 90px; right: 90px;
    top: 268px;
    display: flex;
    align-items: center;
    gap: 14px;
    color: var(--ink-light);
    font-size: 13px;
    letter-spacing: 5px;
  }
  .card--front .web-line::before,
  .card--front .web-line::after {
    content: "";
    flex: 1;
    height: 1px;
    background: var(--rule);
  }

  /* Info side */
  .card--back {
    left: 470px;
    top: 510px;
    background: var(--back-card);
  }
  .card--back .brand-name {
    position: absolute;
    right: 60px;
    top: 52px;
    font-weight: 700;
    font-size: 60px;
    letter-spacing: 2px;
    color: var(--ink-light);
  }
  .card--back .divider {
    position: absolute;
    left: 60px; right: 40px;
    top: 150px;
    height: 1px;
    background: var(--rule);
  }
  .contact {
    position: absolute;
    left: 40px;
    bottom: 34px;
    color: var(--ink-soft);
  }
  .contact .person {
    font-size: 22px;
    color: var(--ink-light);
    margin-bottom: 6px;
  }
  .contact .person .role { font-size: 15px; color: var(--ink-soft); }
  .contact .underline {
    width: 360px;
    height: 1px;
    background: var(--rule);
    margin-bottom: 10px;
  }
  .contact .row { font-size: 15px; line-height: 24px; white-space: nowrap; }
  .contact .row span + span { margin-left: 10px; }
</style>
</head>
<body>
<main class="canvas">
  <section class="card card--front" aria-label="Card front">
    <div class="brand-name">Q-ROLLS</div>
    <div class="web-line">www.Q-rolls-example.com</div>
  </section>

  <section class="card card--back" aria-label="Card info side">
    <div class="brand-name">Q-ROLLS</div>
    <div class="divider"></div>
    <div class="contact">
      <div class="person">Tomas Velder <span class="role">- CEO/Founder</span></div>
      <div class="underline"></div>
      <div class="row"><span>M : 630-812-4463</span><span>P : 630-917-3384 EXT. 417</span></div>
      <div class="row"><span>E : Tomas@q-rolls-example.com</span><span>W : www.Q-rolls-example.com</span></div>
    </div>
  </section>
</main>
</body>
</html>
```